Web Design For Metal Recycling Company

We are a scrap and recycling company dealing mainly in scrap metal base in Singapore. We deal in both domestic market and international market. Currently we are still unsure if we want to have a "lively" or "professional" company image so we will leave it to the designer to deem what is good.

We wish for a website to be able to "Retain" the interest of new visitor and at the same time able to give enough information for new and existing customer. We would also wish for design that will get the visitor to "Engage" us.

The attached is the logo for the company and we would want to incorporate that into the website. Either of the logo is fine.

```html
<!DOCTYPE html>
<html lang="en">
<head>
<meta charset="utf-8">
<title>Ferrona — Metal Recycling</title>
<link href="https://fonts.googleapis.com/css2?family=Roboto+Condensed:wght@300;400;700&family=Roboto:wght@400;700&display=swap" rel="stylesheet">
<style>
:root{
  --teal:#0e4651;
  --teal-deep:#0b3a44;
  --green:#3cb04a;
  --green-soft:#4caf50;
  --ink:#1d1d1d;
  --card:#2e2e2e;
  --paper:#f7f7f7;
  --white:#ffffff;
  --footer:#1e1e1e;
  --gold:#d9a124;
}
*{margin:0;padding:0;box-sizing:border-box}
html,body{width:1200px;height:2245px;overflow:hidden}
body{position:relative;background:var(--paper);font-family:"Roboto",Arial,sans-serif;color:var(--ink)}
.abs{position:absolute}
.top-rule{left:0;top:0;width:1200px;height:12px;background:var(--teal)}
.brand{left:167px;top:40px;display:flex;align-items:center;gap:14px;font-family:"Roboto Condensed",sans-serif;font-weight:700;font-size:40px;color:var(--gold)}
.brand-square{width:24px;height:24px;border:0;background:var(--gold)}
.follow{left:900px;top:30px;display:flex;align-items:center;gap:8px;font-size:15px;color:#333}
.follow .dot{width:28px;height:28px;border:2px solid #333;border-radius:50%}
.search{left:836px;top:77px;width:204px;height:38px;display:flex}
.search-field{flex:1;border:2px solid #5d8d97;background:#fff;font-size:13px;color:#9bb;padding:9px 8px;font-family:"Roboto Condensed",sans-serif}
.search-btn{width:40px;background:var(--teal);display:flex;align-items:center;justify-content:center}
.main-nav{left:0;top:175px;width:1200px;height:45px;background:var(--teal)}
.main-nav a{position:absolute;top:13px;color:#fff;text-decoration:none;font-family:"Roboto Condensed",sans-serif;font-size:15px;font-weight:700;transform:translateX(-50%)}
.main-nav a.current{border-bottom:2px solid var(--green);padding-bottom:4px}
.hero{left:0;top:230px;width:1200px;height:526px;background:linear-gradient(90deg,#3c64b0 0%,#6a8fc4 22%,#8a5a58 40%,#4a9ca3 65%,#9b4e3a 100%)}
.hero-shade{left:0;top:230px;width:1200px;height:526px;background:linear-gradient(180deg,rgba(0,0,0,0) 40%,rgba(0,0,0,.35) 100%)}
.arrow{top:499px;width:43px;height:42px;background:#111;display:flex;align-items:center;justify-content:center}
.hero-title{left:252px;top:528px;width:560px;color:#fff;font-weight:700;font-size:48px;line-height:56px}
.hero-sub{left:258px;top:660px;color:#fff;font-size:22px}
h2{font-family:"Roboto Condensed",sans-serif;font-weight:300;font-size:46px;line-height:1}
.what-title{left:180px;top:812px;color:#111}
.what-sub{left:180px;top:872px;font-size:15px;color:#222}
.card{top:946px;width:262px;height:314px;background:var(--card)}
.card-img{width:262px;height:164px}
.card-label{height:30px;background:var(--green);color:#fff;font-family:"Roboto Condensed",sans-serif;font-weight:700;font-size:17px;text-align:center;line-height:30px}
.card-text{padding:12px 20px 0;color:#ccc;font-size:11px;line-height:20px;text-align:center}
.card-more{margin-top:20px;color:#fff;font-family:"Roboto Condensed",sans-serif;font-weight:700;font-size:13px;text-align:center;letter-spacing:1px}
.services{left:0;top:1322px;width:1200px;height:544px;background:var(--teal)}
.services-title{left:180px;top:1358px;color:#fff}
.services-sub{left:180px;top:1420px;color:var(--green);font-size:15px}
.svc-icon{width:58px;height:58px}
.svc-head{color:var(--green);font-family:"Roboto Condensed",sans-serif;font-weight:700;font-size:27px}
.svc-text{color:#fff;font-size:13px;line-height:20px;width:260px;margin-top:6px}
.svc-rule{left:212px;top:1664px;width:786px;height:1px;background:rgba(255,255,255,.15)}
.partners-title{left:180px;top:1902px;color:#111}
.badge{top:1988px;width:90px;height:90px;border-radius:50%;background:var(--green-soft)}
.foot-nav{left:0;top:2128px;width:1200px;height:47px;background:var(--green)}
.foot-nav a{position:absolute;top:14px;color:#fff;text-decoration:none;font-family:"Roboto Condensed",sans-serif;font-weight:700;font-size:14px}
.foot-follow{left:831px;top:2143px;color:#e6f5e6;font-size:13px}
.foot-social{top:2138px;width:28px;height:28px;background:#3a5ba0}
.foot-base{left:0;top:2175px;width:1200px;height:70px;background:var(--footer);color:#ddd;font-size:13px;text-align:center;line-height:70px}
</style>
</head>
<body>
<div class="abs top-rule"></div>

<div class="abs brand"><span class="brand-square"></span>Ferrona</div>
<div class="abs follow">Follow Us: <span class="dot"></span><span class="dot"></span></div>
<div class="abs search">
  <div class="search-field">SEARCH</div>
  <div class="search-btn"><svg width="22" height="22" viewBox="0 0 22 22"><circle cx="9" cy="9" r="6" fill="none" stroke="#fff" stroke-width="3"/><line x1="13.5" y1="13.5" x2="20" y2="20" stroke="#fff" stroke-width="3.5"/></svg></div>
</div>

<nav class="abs main-nav">
  <a class="current" style="left:404px">HOME</a>
  <a style="left:494px">WHAT WE DO</a>
  <a style="left:584px">SERVICES</a>
  <a style="left:676px">LOCATION</a>
  <a style="left:771px">CONTACT US</a>
</nav>

<div class="abs hero" role="img" aria-label="Photo of a man dropping a bottle into a recycling bank"></div>
<div class="abs hero-shade"></div>
<div class="abs arrow" style="left:87px"><svg width="16" height="20"><path d="M12 2 L4 10 L12 18" fill="none" stroke="#fff" stroke-width="3"/></svg></div>
<div class="abs arrow" style="left:1065px"><svg width="16" height="20"><path d="M4 2 L12 10 L4 18" fill="none" stroke="#fff" stroke-width="3"/></svg></div>
<div class="abs hero-title">Lorem ipsum dolor sit amet, consectetur</div>
<div class="abs hero-sub">Lorem ipsum dolor sit amet, consectetur adipisicing elit</div>

<h2 class="abs what-title">WHAT WE DO</h2>
<p class="abs what-sub">Lorem ipsum dolor sit amet, consectetur adipisicing elit.</p>

<div class="abs card" style="left:180px">
  <div class="card-img" role="img" aria-label="Photo of colourful recycling bins" style="background:linear-gradient(90deg,#3b78c0,#e0c040,#5aa84a,#c83a3a)"></div>
  <div class="card-label">LOREM IPSUM DOLOR</div>
  <p class="card-text">Sed ut perspiciatis unde omnis iste natus error sit voluptatem accusantium doloremque.</p>
  <div class="card-more">READ MORE</div>
</div>
<div class="abs card" style="left:472px">
  <div class="card-img" role="img" aria-label="Photo of workers sorting material at a recycling plant" style="background:linear-gradient(180deg,#7d7a6a,#9b9886)"></div>
  <div class="card-label">LOREM IPSUM DOLOR</div>
  <p class="card-text">Sed ut perspiciatis unde omnis iste natus error sit voluptatem accusantium doloremque.</p>
  <div class="card-more">READ MORE</div>
</div>
<div class="abs card" style="left:761px">
  <div class="card-img" role="img" aria-label="Photo of a business team" style="background:linear-gradient(180deg,#f2f2f2,#3a3a3a)"></div>
  <div class="card-label">LOREM IPSUM DOLOR</div>
  <p class="card-text">Sed ut perspiciatis unde omnis iste natus error sit voluptatem accusantium doloremque.</p>
  <div class="card-more">READ MORE</div>
</div>

<section class="abs services"></section>
<h2 class="abs services-title">SERVICES</h2>
<p class="abs services-sub">Lorem ipsum dolor sit amet, consectetur adipisicing elit, sed do eiusmod tempor incididunt ut labore et dolore.</p>

<div class="abs" style="left:222px;top:1505px;display:flex;gap:8px">
  <svg class="svc-icon" viewBox="0 0 58 58"><g fill="none" stroke="#fff" stroke-width="6"><path d="M18 20 L26 8 L34 20"/><path d="M44 28 L48 44 L34 44"/><path d="M14 44 L8 32 L20 28"/></g></svg>
  <div><div class="svc-head">LOREM IPSUM</div><p class="svc-text">Lorem ipsum dolor sit amet, consectetur adipisicing elit, sed do eiusmod tempor.</p></div>
</div>
<div class="abs" style="left:679px;top:1505px;display:flex;gap:10px">
  <svg class="svc-icon" viewBox="0 0 58 58" fill="#fff"><circle cx="14" cy="18" r="6"/><circle cx="29" cy="14" r="8"/><circle cx="44" cy="18" r="6"/><path d="M4 38 Q14 24 24 38Z"/><path d="M16 38 Q29 18 42 38Z"/><path d="M34 38 Q44 24 54 38Z"/></svg>
  <div><div class="svc-head">LOREM IPSUM</div><p class="svc-text">Lorem ipsum dolor sit amet, consectetur adipisicing elit, sed do eiusmod tempor.</p></div>
</div>
<div class="abs svc-rule"></div>
<div class="abs" style="left:222px;top:1695px;display:flex;gap:8px">
  <svg class="svc-icon" viewBox="0 0 58 58" fill="#fff"><circle cx="32" cy="8" r="5"/><rect x="28" y="15" width="9" height="22"/><rect x="29" y="37" width="3" height="18"/><rect x="33" y="37" width="3" height="18"/><path d="M10 32 H24 L22 54 H12Z"/></svg>
  <div><div class="svc-head">LOREM IPSUM</div><p class="svc-text">Lorem ipsum dolor sit amet, consectetur adipisicing elit, sed do eiusmod tempor.</p></div>
</div>
<div class="abs" style="left:679px;top:1695px;display:flex;gap:10px">
  <svg class="svc-icon" viewBox="0 0 58 58"><path d="M8 30 L22 44 L50 12" fill="none" stroke="#fff" stroke-width="8"/></svg>
  <div><div class="svc-head">LOREM IPSUM</div><p class="svc-text">Lorem ipsum dolor sit amet, consectetur adipisicing elit, sed do eiusmod tempor.</p></div>
</div>

<h2 class="abs partners-title">OUR PARTNERS</h2>
<div class="abs badge" style="left:242px"></div>
<div class="abs badge" style="left:392px"></div>
<div class="abs badge" style="left:541px"></div>
<div class="abs badge" style="left:691px"></div>
<div class="abs badge" style="left:841px"></div>

<footer>
  <nav class="abs foot-nav">
    <a style="left:180px">HOME</a>
    <a style="left:245px">WHAT WE DO</a>
    <a style="left:349px">SERVICES</a>
    <a style="left:439px">LOCATION</a>
    <a style="left:529px">CONTACT US</a>
  </nav>
  <div class="abs foot-follow">Follow Us:</div>
  <div class="abs foot-social" style="left:893px"></div>
  <div class="abs foot-social" style="left:926px;background:#3aa7d8"></div>
  <div class="abs foot-social" style="left:959px;background:#2f6fa8"></div>
  <div class="abs foot-social" style="left:992px;background:#444"></div>
  <div class="abs foot-base">Privacy | Copyright</div>
</footer>
</body>
</html>
```